Geschäftspapiere für Immobilienmakler
Zielgruppe
'BRAVOK Immobilien' Immobilienmakler in Aachen und der Region macht Verkauf - Vermietung und Gutachten von Immobilien
Aufgabenstellung
'BRAVOK Immobilien' ist der Firmenname und soll auch so bleiben. Ein Logo (Abkürzung) dazu fehlt mir noch. Briefpapier,Umschläge & Co sowie eine Excel Vorlage mit Design zur Rechnungserstellung wird ebenfalls benötigt.
(Optional: Eventuell einen Sticker für Social Media von mir mit einem Schild mit (Sold ! oder NEW!))

```html
<!DOCTYPE html>
<html lang="de">
<head>
<meta charset="utf-8">
<title>BRAVOK Immobilien – Geschäftspapiere</title>
<link rel="stylesheet" href="https://fonts.googleapis.com/css2?family=Playfair+Display:wght@400&family=Montserrat:wght@400;500;600&display=swap">
<style>
  :root {
    --navy: #151f38;
    --sand: #d6cfc5;
    --paper: #ffffff;
    --stage: #f7f7f7;
    --rule: #8a8d9c;
    --ghost: #f1f1f1;
    --footer-text: #e6e8ee;
    --footer-muted: #a7adbd;
  }
  * { margin: 0; padding: 0; box-sizing: border-box; }
  html, body { width: 1200px; height: 765px; overflow: hidden; background: var(--stage); }
  body { position: relative; font-family: "Montserrat", sans-serif; color: var(--navy); }

  .sheet { position: absolute; background: var(--paper); box-shadow: 4px 10px 24px rgba(0,0,0,0.12); overflow: hidden; }

  /* Brand name */
  .brand { font-family: "Playfair Display", serif; font-weight: 400; color: var(--navy); text-align: center; line-height: 1; }
  .brand-name { display: block; font-size: 32px; letter-spacing: 0.42em; margin-right: -0.42em; }
  .brand-sub { display: block; font-size: 7px; letter-spacing: 0.5em; margin-right: -0.5em; margin-top: 9px; }

  /* Letterhead */
  .letterhead { left: 134px; top: 104px; width: 394px; height: 558px; }
  .letterhead .brand { position: absolute; left: 0; right: 0; top: 22px; }
  .letterhead-rule { position: absolute; left: 26px; width: 344px; top: 86px; height: 1px; background: var(--rule); }
  .letter-date { position: absolute; right: 24px; top: 118px; font-size: 6.5px; font-weight: 600; }
  .letter-watermark { position: absolute; left: 0; right: 0; top: 160px; text-align: center; font-family: "Playfair Display", serif; font-size: 88px; color: var(--ghost); letter-spacing: 0.05em; line-height: 1; }

  .letter-footer { position: absolute; left: 0; right: 0; bottom: 0; height: 92px; background: var(--navy); color: var(--footer-text); font-size: 5.6px; }
  .letter-footer .row-top { position: absolute; left: 25px; right: 24px; top: 14px; display: flex; justify-content: space-between; font-weight: 600; }
  .letter-footer .spaced { letter-spacing: 0.22em; }
  .letter-footer .footer-rule { position: absolute; left: 25px; right: 24px; top: 25px; height: 1px; background: var(--footer-muted); }
  .letter-footer .email { position: absolute; left: 25px; top: 32px; font-weight: 600; }
  .footer-col { position: absolute; top: 49px; line-height: 10px; color: var(--footer-muted); }
  .footer-col b { color: var(--footer-text); font-weight: 600; }
  .col-phone { left: 25px; }
  .col-phone .indent { padding-left: 14px; }
  .col-bank { left: 150px; top: 51px; }
  .col-register { left: 275px; top: 51px; }

  /* Envelope front */
  .envelope-front { left: 654px; top: 102px; width: 413px; height: 188px; }
  .envelope-front .brand { position: absolute; left: 20px; top: 28px; width: 170px; }
  .address-window { position: absolute; left: 223px; top: 95px; width: 169px; height: 53px; border-radius: 8px; background: var(--sand); }
  .sender-band { position: absolute; left: 0; right: 0; bottom: 0; height: 20px; background: var(--navy); color: #fff; font-size: 8.5px; padding-left: 18px; line-height: 20px; letter-spacing: 0.02em; }

  /* Envelope back */
  .envelope-back { left: 654px; top: 337px; width: 413px; height: 188px; }
  .envelope-flap { position: absolute; left: 0; top: 0; }
  .flap-name { position: absolute; left: 0; right: 0; top: 26px; text-align: center; font-family: "Playfair Display", serif; font-size: 16px; letter-spacing: 0.3em; margin-right: -0.3em; color: var(--sand); }
  .website { position: absolute; left: 0; right: 0; top: 165px; text-align: center; font-size: 9px; letter-spacing: 0.42em; margin-right: -0.42em; }
</style>
</head>
<body>

  <section class="sheet letterhead" aria-label="Briefpapier">
    <h1 class="brand"><span class="brand-name">BRAVOK</span><span class="brand-sub">IMMOBILIEN</span></h1>
    <div class="letterhead-rule"></div>
    <p class="letter-date">Datum. 05.05.2026</p>
    <div class="letter-watermark" aria-hidden="true">BRAVOK</div>

    <footer class="letter-footer">
      <div class="row-top">
        <span>Geschäftsführung : <span class="spaced">Bravok Immobilien</span></span>
        <span>Firmensitz : Lindenweg 14, 52064 Aachen</span>
      </div>
      <div class="footer-rule"></div>
      <p class="email">info@bravokimmobilien.de</p>
      <p class="footer-col col-phone"><b>Tel :</b> +49 241 5550 1240<br><span class="indent">+49 151 0000 0000</span></p>
      <p class="footer-col col-bank">Regionalbank <b>Wurmtal</b><br><b>IBAN :</b> DExxxxxxxxxxxxxxxxx<br><b>BIC :</b> GExxxxxxxxx</p>
      <p class="footer-col col-register"><b>Amtsgericht Aachen</b> HRB xxxxxx<br>Steuer-Nr. xxxxx/xxxxx<br>Ust-IdNr. DExxxxxxxxx</p>
    </footer>
  </section>

  <section class="sheet envelope-front" aria-label="Briefumschlag Vorderseite">
    <div class="brand"><span class="brand-name">BRAVOK</span><span class="brand-sub">IMMOBILIEN</span></div>
    <div class="address-window"></div>
    <div class="sender-band">Lindenweg 14, 52064 Aachen</div>
  </section>

  <section class="sheet envelope-back" aria-label="Briefumschlag Rückseite">
    <svg class="envelope-flap" width="413" height="68" viewBox="0 0 413 68" aria-hidden="true">
      <path d="M0 0 H413 L407 56 Q405 68 393 68 H20 Q8 68 6 56 Z" fill="var(--navy)"/>
    </svg>
    <div class="flap-name">BRAVOK</div>
    <p class="website">www.bravokimmobilien.de</p>
  </section>

</body>
</html>
```